Brightpath7crew needs a website

We need a website so we can post future events of our company about business motivation. The site have to include a calendar on the "Home" page that when the user cliks on the day of the event , there should open a small page with the information of the event (location,time,subject of the event...) . We need also an "About Us" page with information about our company and what we do as well as "Contact" page with our email and phone number and access to our facebook page. We would like to have a private access for users ("Restricted access") but they have to put their e-mail and password to access the special page (log in). On the 'special page' we would like to have some videos and photos that we will post on that page regularly .
Here is a website that would be an exemple of how we would like to have ours
http://summitlarkacademy.example
The needs to be responsed and with backoffice

Industry/Entity Type

Business

Number of Pages Required

3 page

Colors
9bcb3c
f37122

Requirements
Must have
• Must have a restricted access page so the user can place a user name and a secret password.

```html
<!DOCTYPE html>
<html lang="en">
<head>
<meta charset="utf-8">
<title>Brightpath7crew – Conference Event</title>
<link href="https://fonts.googleapis.com/css2?family=Montserrat:wght@400;600;700&family=Open+Sans:wght@400;600&display=swap" rel="stylesheet">
<style>
:root{
  --green:#9bcb3c;
  --orange:#f37122;
  --dark:#2b2b2b;
  --darker:#222;
  --ink:#333;
  --muted:#8a8a8a;
  --light:#f4f4f4;
  --white:#fff;
}
*{box-sizing:border-box;margin:0;padding:0}
html,body{width:669px;height:1200px;overflow:hidden;background:var(--white)}
body{font-family:"Open Sans",Arial,sans-serif;color:var(--ink);font-size:7px;line-height:1.45}
h1,h2,h3,h4,.brand,.nav a{font-family:"Montserrat",Arial,sans-serif}

.site-header{height:40px;display:flex;align-items:center;justify-content:space-between;padding:0 128px 0 132px;background:var(--white)}
.brand{display:flex;align-items:center;gap:6px;font-weight:700;font-size:12px;color:var(--green);letter-spacing:.3px}
.brand-mark{width:16px;height:16px;background:var(--green)}
.nav{display:flex;height:40px}
.nav a{display:flex;align-items:center;padding:0 9px;font-size:7px;font-weight:600;color:var(--ink);text-decoration:none}
.nav a.active{background:var(--orange);color:var(--white)}

.hero{position:relative;height:222px;background:linear-gradient(90deg,#3a2a24 0%,#5b4638 40%,#27384e 70%,#1c2536 100%)}
.hero-content{position:absolute;left:145px;top:18px;color:var(--white)}
.hero h1{font-size:15px;font-weight:700;margin-bottom:10px}
.hero .label{font-size:7px;color:#ddd}
.hero .value{font-size:10px;color:var(--orange);margin-bottom:6px}
.btn{display:inline-block;background:var(--green);color:var(--white);font-family:"Montserrat",sans-serif;font-weight:600;font-size:6.5px;padding:5px 10px;border-radius:2px}

.countdown{height:50px;background:var(--orange);display:flex;align-items:center;justify-content:center;gap:14px;color:var(--white)}
.countdown h3{font-size:10px;font-weight:600;margin-right:14px}
.count-box{width:26px;height:26px;border:1px solid rgba(255,255,255,.7);display:flex;flex-direction:column;align-items:center;justify-content:center;font-family:"Montserrat",sans-serif;font-size:9px;font-weight:700;line-height:1}
.count-box small{font-size:4px;font-weight:400;margin-top:2px}
.countdown .btn{margin-left:14px}

.features{height:145px;display:flex;justify-content:center;gap:26px;padding-top:22px;background:var(--white)}
.feature{width:100px;text-align:center}
.feature-icon{width:28px;height:28px;border-radius:50%;border:2px solid var(--orange);margin:0 auto 7px;display:flex;align-items:center;justify-content:center}
.feature h4{font-size:7px;font-weight:700;margin-bottom:4px}
.feature p{color:var(--muted);font-size:5.5px}

.section-title{font-size:12px;font-weight:700;text-align:center;letter-spacing:.5px}
.events-title{margin-top:-8px;margin-bottom:10px}
.event-strip{display:flex;height:117px}
.event-photo{flex:1}
.event-feature{width:167px;background:var(--orange);color:var(--white);display:flex;flex-direction:column;align-items:center;justify-content:center;text-align:center;padding:0 18px}
.event-feature h4{font-size:7px;font-weight:700;margin-bottom:4px}
.event-feature p{font-size:5px}

.about{padding-top:22px;text-align:center}
.about-intro{width:300px;margin:6px auto 14px;color:var(--muted);font-size:5.5px}
.about-cards{display:flex;justify-content:center;gap:12px}
.about-card{width:91px;text-align:left}
.about-photo{height:77px;margin-bottom:5px}
.about-card h4{font-size:6px;font-weight:700;margin-bottom:2px}
.about-card p{font-size:5px;color:var(--muted)}

.video{margin-top:16px;height:167px;background:radial-gradient(circle at 50% 60%,#8fc23a,#76a82c);padding-top:12px;text-align:center;color:var(--white)}
.video .section-title{color:var(--white)}
.video-frame{position:relative;width:184px;height:102px;margin:8px auto 0;background:linear-gradient(135deg,#1d2340,#3b3f8a 55%,#141629)}
.play{position:absolute;left:84px;top:43px;width:16px;height:16px;border-radius:50%;background:var(--orange);display:flex;align-items:center;justify-content:center}

.site-footer{display:flex;height:189px}
.footer-info{width:333px;background:var(--darker);color:#ccc;display:flex;gap:24px;padding:32px 0 0 70px}
.footer-col{width:110px}
.footer-col .kicker{font-size:5px;color:var(--orange)}
.footer-col h3{font-size:10px;color:var(--white);font-weight:700;margin-bottom:10px}
.footer-line{display:flex;gap:5px;align-items:flex-start;font-size:5px;margin-bottom:8px}
.dot{width:6px;height:6px;border-radius:50%;background:var(--orange);flex:none;margin-top:1px}
.tweet{font-size:5px;margin-bottom:10px}
.tweet span{color:var(--orange)}
.footer-map{flex:1;background:linear-gradient(135deg,#e8e6df,#d8dde4 50%,#cfd9c4);position:relative}
.map-pin{position:absolute;left:160px;top:70px}
.legal{height:30px;background:var(--orange);color:var(--white);font-size:5px;display:flex;align-items:center;justify-content:center}
</style>
</head>
<body>
<header class="site-header">
  <div class="brand"><span class="brand-mark"></span>Brightpath7crew</div>
  <nav class="nav">
    <a class="active" href="#">HOME</a><a href="#">ABOUT US</a><a href="#">MEETINGS</a><a href="#">EVENTS</a><a href="#">RESOURCES</a><a href="#">CONTACT</a>
  </nav>
</header>

<section class="hero" role="img" aria-label="Speaker addressing a conference audience from a stage">
  <div class="hero-content">
    <h1>CONFERENCE EVENT</h1>
    <div class="label">Event Name</div>
    <div class="value">Summit Motivation Event</div>
    <div class="label">Event Date</div>
    <div class="value">12 March 2025</div>
    <div class="label">Event Location</div>
    <div class="value">Lakeside Forum Hall Northgate</div>
    <span class="btn">VIEW MORE</span>
  </div>
</section>

<section class="countdown">
  <h3>Time Left To Conference</h3>
  <div class="count-box">111<small>DAYS</small></div>
  <div class="count-box">12<small>HOURS</small></div>
  <div class="count-box">36<small>MINS</small></div>
  <div class="count-box">52<small>SECS</small></div>
  <span class="btn">REGISTER</span>
</section>

<section class="features">
  <div class="feature">
    <div class="feature-icon"><svg width="12" height="12" viewBox="0 0 12 12"><circle cx="6" cy="4" r="2.5" fill="#f37122"/><path d="M1 12c0-3 2.2-5 5-5s5 2 5 5z" fill="#f37122"/></svg></div>
    <h4>20+ SPEAKERS</h4><p>Inspiring voices share practical growth ideas for business leaders and teams.</p>
  </div>
  <div class="feature">
    <div class="feature-icon"><svg width="12" height="12" viewBox="0 0 12 12"><rect x="1" y="2" width="10" height="9" fill="none" stroke="#f37122" stroke-width="1.4"/><path d="M1 5h10" stroke="#f37122" stroke-width="1.4"/></svg></div>
    <h4>26+ EVENTS</h4><p>Workshops and sessions planned across the year for every member.</p>
  </div>
  <div class="feature">
    <div class="feature-icon"><svg width="12" height="12" viewBox="0 0 12 12"><rect x="1" y="2" width="10" height="9" fill="none" stroke="#f37122" stroke-width="1.4"/><path d="M3.5 7l2 2 3-4" fill="none" stroke="#f37122" stroke-width="1.4"/></svg></div>
    <h4>5+ EVENTS</h4><p>Focused masterclasses on motivation, planning and team success.</p>
  </div>
  <div class="feature">
    <div class="feature-icon"><svg width="12" height="12" viewBox="0 0 12 12"><path d="M6 1l1.5 3.2 3.5.4-2.6 2.4.7 3.5L6 8.8 2.9 10.5l.7-3.5L1 4.6l3.5-.4z" fill="#f37122"/></svg></div>
    <h4>PARTY EVENTS</h4><p>Relaxed evening gatherings to meet peers and build connections.</p>
  </div>
</section>

<h2 class="section-title events-title">CONFERENCE EVENTS</h2>
<section class="event-strip">
  <div class="event-photo" role="img" aria-label="Audience seated in a conference hall" style="background:linear-gradient(135deg,#4a4f5c,#8a7e74)"></div>
  <div class="event-feature">
    <h4>OUR 1ST CONFERENCE</h4>
    <p>Our first gathering brought together founders and teams to share ideas on growth.</p>
  </div>
  <div class="event-photo" role="img" aria-label="Crowded conference room during a session" style="background:linear-gradient(135deg,#7d6b5e,#3f4450)"></div>
  <div class="event-photo" role="img" aria-label="Attendees networking at an event" style="background:linear-gradient(135deg,#56606d,#a79a8d)"></div>
</section>

<section class="about">
  <h2 class="section-title">ABOUT OUR CONFERENCE</h2>
  <p class="about-intro">We host motivating business events that help people plan, grow and lead with confidence, and share fresh tools for every stage of their career.</p>
  <div class="about-cards">
    <div class="about-card"><div class="about-photo" role="img" aria-label="Presenter speaking to a group" style="background:linear-gradient(135deg,#6d7480,#c2b6a8)"></div><h4>We Offer To You</h4><p>Clear sessions with useful tips you can apply right away.</p></div>
    <div class="about-card"><div class="about-photo" role="img" aria-label="Team meeting around a table" style="background:linear-gradient(135deg,#8a8f96,#d3cdc4)"></div><h4>We Are The Best</h4><p>Trusted hosts with years of event experience behind us.</p></div>
    <div class="about-card"><div class="about-photo" role="img" aria-label="Speaker on stage before a screen" style="background:linear-gradient(135deg,#3e4a63,#9aa4b4)"></div><h4>Interesting Info</h4><p>Fresh insights and stories from leaders in many fields.</p></div>
    <div class="about-card"><div class="about-photo" role="img" aria-label="Woman presenting at a workshop" style="background:linear-gradient(135deg,#b6aea3,#6a6e76)"></div><h4>Our History</h4><p>Growing since our first event with a loyal community.</p></div>
  </div>
</section>

<section class="video">
  <h2 class="section-title">OUR VIDEO</h2>
  <div class="video-frame" role="img" aria-label="Video still of a large stage with a projected screen">
    <span class="play"><svg width="7" height="7" viewBox="0 0 7 7"><path d="M1.5 0.5L6.5 3.5 1.5 6.5z" fill="#fff"/></svg></span>
  </div>
</section>

<footer class="site-footer">
  <div class="footer-info">
    <div class="footer-col">
      <div class="kicker">Connect Now</div>
      <h3>CONTACT US</h3>
      <p class="footer-line" style="color:#999">Reach our team any weekday for event details and bookings.</p>
      <div class="footer-line"><span class="dot"></span>1420 Harbor Lane, Northgate</div>
      <div class="footer-line"><span class="dot"></span>hello@brightpath7crew.example</div>
      <div class="footer-line"><span class="dot"></span>+1 (555) 014 2286</div>
    </div>
    <div class="footer-col">
      <div class="kicker">Latest</div>
      <h3>OUR CHIRPLINE</h3>
      <p class="tweet"><span>@brightpath7crew</span> New dates for our spring summit are now open.</p>
      <p class="tweet"><span>@brightpath7crew</span> Thank you to everyone who joined our last workshop.</p>
    </div>
  </div>
  <div class="footer-map" role="img" aria-label="Street map showing the venue location">
    <svg class="map-pin" width="14" height="18" viewBox="0 0 14 18"><path d="M7 0C3 0 0 3 0 7c0 5 7 11 7 11s7-6 7-11c0-4-3-7-7-7z" fill="#f37122"/><circle cx="7" cy="7" r="2.5" fill="#fff"/></svg>
  </div>
</footer>
<div class="legal">Brightpath7crew © 2025 All rights reserved</div>
</body>
</html>
```